Refresh Application User Interface

Pellmark wishes to update the look of its business applications. Two representative forms are shown below. Please note, we are not considering changes in functionality or usability. Our goal is a cleaner, more contemporary design.

Industry/Entity Type

Business

```html
<!DOCTYPE html>
<html lang="en">
<head>
<meta charset="utf-8">
<title>Pellmark – Purchase Order</title>
<link href="https://fonts.googleapis.com/css2?family=Roboto:wght@400;500;700;900&display=swap" rel="stylesheet">
<style>
:root{
  --brand-blue:#0a4fa0;
  --deep-blue:#07489a;
  --nav-blue:#0c4a93;
  --tab-blue:#0d3f82;
  --green:#97c95c;
  --panel:#f6f6f6;
  --field-border:#d4d4d4;
  --text:#222;
  --muted-btn:#efefef;
}
*{box-sizing:border-box;margin:0;padding:0}
html,body{width:1200px;height:1182px;overflow:hidden;background:#fff;font-family:'Roboto',sans-serif;color:var(--text)}
.abs{position:absolute}
.header{position:absolute;left:0;top:0;width:1200px;height:55px;background:#fff;box-shadow:0 2px 3px rgba(0,0,0,.12);z-index:2}
.logo{left:22px;top:10px;font-size:28px;font-weight:900;color:var(--brand-blue);letter-spacing:.5px;display:flex;align-items:center;gap:8px}
.logo .dot{width:12px;height:12px;border-radius:50%;background:var(--green)}
.user{top:19px;font-size:12.5px;white-space:nowrap}
.user b{color:var(--brand-blue);font-weight:500}
.circle-btn{width:26px;height:26px;border-radius:50%;background:var(--brand-blue);display:flex;align-items:center;justify-content:center;box-shadow:0 2px 3px rgba(0,0,0,.25)}
.toplinks{left:828px;top:19px;font-size:12px;color:#333;display:flex;gap:12px;white-space:nowrap}
.logout{left:1078px;top:9px;width:103px;height:36px;background:var(--brand-blue);color:#fff;font-size:11px;font-weight:700;display:flex;align-items:center;justify-content:center}
.nav{left:0;top:55px;width:1200px;height:75px;background:var(--nav-blue)}
.nav .tab{position:absolute;top:24px;height:31px;background:var(--tab-blue);color:#fff;font-size:13px;display:flex;align-items:center;justify-content:center}
.nav .tab.active{background:var(--green)}
.nav .caret{position:absolute;left:267px;top:68px;width:0;height:0;border-left:5px solid transparent;border-right:5px solid transparent;border-bottom:7px solid var(--green)}
.subnav{left:0;top:130px;width:1200px;height:40px;background:var(--green)}
.subnav span{position:absolute;top:12px;color:#fff;font-size:13px;font-weight:500;white-space:nowrap}
.page-title{left:21px;top:192px;font-size:21px;font-weight:700;color:var(--brand-blue)}
.view-btn{top:185px;width:102px;height:36px;background:var(--muted-btn);border:1px solid #e2e2e2;font-size:12.5px;display:flex;align-items:center;justify-content:center;color:#333}
.view-btn.active{background:var(--brand-blue);color:#fff;border-color:var(--brand-blue)}
.toolbar{left:19px;top:237px;width:1162px;height:46px;background:var(--deep-blue)}
.tool{position:absolute;top:0;height:46px;border-right:1px solid #1e5eaa;display:flex;align-items:center;justify-content:center;color:#fff;font-size:12.5px;gap:12px}
.action{position:absolute;top:10px;display:flex;align-items:center;gap:10px;color:#fff;font-size:12.5px}
.action .ic{width:26px;height:26px;border-radius:50%;background:#fff;display:flex;align-items:center;justify-content:center}
.sheet{left:19px;top:283px;width:1162px;height:899px;background:var(--panel);box-shadow:inset 0 6px 6px -4px rgba(0,0,0,.12)}
.lbl{position:absolute;font-size:12px;text-align:right;width:200px}
.input{position:absolute;height:38px;background:#fff;border:1px solid var(--field-border);border-radius:2px}
.ftab{position:absolute;top:668px;height:37px;background:var(--muted-btn);border:1px solid #e2e2e2;font-size:12px;display:flex;align-items:center;justify-content:center;color:#333}
.ftab.active{background:var(--brand-blue);color:#fff;border-color:var(--brand-blue);height:42px}
.ship{left:52px;top:710px;width:1110px;height:385px;background:var(--brand-blue)}
.slbl{position:absolute;font-size:12px;color:#fff;font-weight:700;text-align:right;width:200px}
.select{position:absolute;height:37px;background:#fff;border-radius:2px;font-size:10.5px;color:#444;padding-left:14px;display:flex;align-items:center}
.select::after{content:"";position:absolute;right:15px;top:17px;border-left:3.5px solid transparent;border-right:3.5px solid transparent;border-top:4px solid #333}
.hint{left:52px;top:1095px;width:1110px;height:57px;background:var(--green);color:#fff;font-size:14px;font-weight:700;display:flex;align-items:center;justify-content:center}
</style>
</head>
<body>
<header class="header">
  <div class="abs logo"><span>PELLMARK</span><span class="dot"></span></div>
  <div class="abs user" style="left:432px">Logged In As <b>Ken Ward</b></div>
  <div class="abs circle-btn" style="left:574px;top:14px">
    <svg width="14" height="14" viewBox="0 0 14 14"><circle cx="7" cy="7" r="4.5" fill="none" stroke="#fff" stroke-width="2.4" stroke-dasharray="2.2 1.3"/><circle cx="7" cy="7" r="1.6" fill="#fff"/></svg>
  </div>
  <div class="abs user" style="left:617px">Current Role <b>Administrator</b></div>
  <div class="abs circle-btn" style="left:772px;top:14px">
    <svg width="10" height="6" viewBox="0 0 10 6"><path d="M0 0h10L5 6z" fill="#fff"/></svg>
  </div>
  <div class="abs toplinks"><span>Touch</span><span>/</span><span>New Tab</span><span>/</span><span>Help</span><span>/</span><span>Support</span></div>
  <div class="abs logout">LOG OUT</div>
</header>

<nav class="abs nav">
  <div class="tab" style="left:22px;width:90px">Home</div>
  <div class="tab" style="left:125px;width:91px">eSource</div>
  <div class="tab active" style="left:227px;width:91px">eBuy</div>
  <div class="tab" style="left:330px;width:91px">eRequest</div>
  <div class="tab" style="left:433px;width:90px">eSell</div>
  <div class="tab" style="left:534px;width:92px">eStock</div>
  <div class="tab" style="left:638px;width:90px">ePlan</div>
  <div class="tab" style="left:740px;width:95px">Preferences</div>
  <div class="caret"></div>
</nav>

<div class="abs subnav">
  <span style="left:26px">Orders</span><span style="left:92px">Receipts</span><span style="left:170px">Shipments</span>
  <span style="left:261px">Invoices</span><span style="left:336px">Pricing</span><span style="left:405px">Tables Reports</span>
  <span style="left:520px">Inquiries</span><span style="left:598px">Periodic Tasks</span><span style="left:711px">Workflows</span>
</div>

<h1 class="abs page-title">PURCHASE ORDER</h1>
<div class="abs view-btn active" style="left:733px">Folder Tabs</div>
<div class="abs view-btn" style="left:848px">Lines</div>
<div class="abs view-btn" style="left:962px">Charges</div>
<div class="abs view-btn" style="left:1077px">Notes</div>

<div class="abs sheet"></div>

<div class="abs toolbar">
  <div class="tool" style="left:0;width:45px"><svg width="12" height="20" viewBox="0 0 12 20"><path d="M3 6v9a3 3 0 0 0 6 0V4a2 2 0 0 0-4 0v10" fill="none" stroke="#fff" stroke-width="1.6"/></svg></div>
  <div class="tool" style="left:45px;width:45px"><svg width="18" height="20" viewBox="0 0 18 20"><path d="M2 1h9l4 4v6M2 1v17h8" fill="none" stroke="#fff" stroke-width="1.4"/><circle cx="12" cy="14" r="3" fill="none" stroke="#fff" stroke-width="1.4"/><path d="M14 16l3 3" stroke="#fff" stroke-width="1.4"/></svg></div>
  <div class="tool" style="left:90px;width:45px"><svg width="18" height="18" viewBox="0 0 18 18"><circle cx="4" cy="9" r="2.6" fill="#fff"/><circle cx="14" cy="3.5" r="2.6" fill="#fff"/><circle cx="14" cy="14.5" r="2.6" fill="#fff"/><path d="M4 9l10-5.5M4 9l10 5.5" stroke="#fff" stroke-width="1.5"/></svg></div>
  <div class="tool" style="left:135px;width:44px"><svg width="20" height="16" viewBox="0 0 20 16"><rect x="1" y="4" width="18" height="11" rx="1.5" fill="#fff"/><rect x="7" y="1" width="6" height="3" fill="none" stroke="#fff" stroke-width="1.5"/><path d="M1 9h18" stroke="#07489a" stroke-width="1.5"/></svg></div>
  <div class="tool" style="left:179px;width:45px;font-size:24px;font-weight:700">?</div>
  <div class="tool" style="left:224px;width:127px"><svg width="26" height="20" viewBox="0 0 26 20"><rect x="1" y="1" width="24" height="18" fill="none" stroke="#fff" stroke-width="1.4"/><path d="M1 5h24" stroke="#fff" stroke-width="1.2"/><circle cx="13" cy="11" r="3.5" fill="none" stroke="#fff" stroke-width="1.4"/><path d="M15.5 13.5l3 3" stroke="#fff" stroke-width="1.4"/></svg>Post Order</div>

  <div class="action" style="left:724px"><span class="ic"><svg width="14" height="14" viewBox="0 0 14 14"><circle cx="6" cy="6" r="4" fill="none" stroke="#97c95c" stroke-width="1.6"/><path d="M9 9l4 4" stroke="#97c95c" stroke-width="1.6"/></svg></span>Search</div>
  <div class="action" style="left:812px"><span class="ic"><svg width="14" height="14" viewBox="0 0 14 14"><path d="M7 1v12M1 7h12" stroke="#97c95c" stroke-width="1.6"/></svg></span>New</div>
  <div class="action" style="left:894px"><span class="ic"><svg width="14" height="14" viewBox="0 0 14 14"><path d="M2 7l3.5 3.5L12 3" fill="none" stroke="#97c95c" stroke-width="1.8"/></svg></span>Apply</div>
  <div class="action" style="left:983px"><span class="ic"><svg width="12" height="12" viewBox="0 0 12 12"><path d="M1 1l10 10M11 1L1 11" stroke="#97c95c" stroke-width="1.6"/></svg></span>Delete</div>
  <div class="action" style="left:1075px"><span class="ic"><svg width="14" height="14" viewBox="0 0 14 14"><path d="M6 2L1 6l5 4V7c4 0 6 1 7 4 0-5-3-7-7-7z" fill="#97c95c"/></svg></span>Back</div>
</div>

<div class="lbl" style="left:36px;top:333px">Order#</div>
<div class="lbl" style="left:39px;top:399px">Ship From</div>
<div class="lbl" style="left:39px;top:466px">Harbor Supply Inc</div>
<div class="lbl" style="left:39px;top:532px">Address</div>
<div class="lbl" style="left:39px;top:599px">City</div>
<div class="input" style="left:253px;top:325px;width:307px"></div>
<div class="input" style="left:253px;top:390px;width:307px"></div>
<div class="input" style="left:253px;top:456px;width:307px"></div>
<div class="input" style="left:253px;top:521px;width:307px"></div>
<div class="input" style="left:253px;top:586px;width:307px"></div>

<div class="lbl" style="left:483px;top:334px">Zip</div>
<div class="lbl" style="left:480px;top:400px">Country</div>
<div class="lbl" style="left:483px;top:467px">State</div>
<div class="lbl" style="left:483px;top:533px">Address</div>
<div class="lbl" style="left:483px;top:600px">Add Contact</div>
<div class="input" style="left:699px;top:325px;width:307px"></div>
<div class="input" style="left:699px;top:390px;width:307px"></div>
<div class="input" style="left:699px;top:456px;width:307px"></div>
<div class="input" style="left:699px;top:521px;width:307px"></div>
<div class="input" style="left:699px;top:586px;width:307px"></div>

<div class="ftab" style="left:52px;width:102px">Order info</div>
<div class="ftab active" style="left:167px;width:103px">Shipping</div>
<div class="ftab" style="left:282px;width:102px">Payment</div>
<div class="ftab" style="left:397px;width:102px">Account</div>
<div class="ftab" style="left:512px;width:130px">Totals / Approval</div>

<section class="abs ship"></section>
<div class="slbl" style="left:30px;top:792px">Recevice At</div>
<div class="slbl" style="left:30px;top:851px">Carrier</div>
<div class="slbl" style="left:30px;top:910px">Express Service</div>
<div class="slbl" style="left:30px;top:970px">Fob</div>
<div class="slbl" style="left:30px;top:1030px">Order Ship Rule</div>
<div class="select" style="left:253px;top:782px;width:305px">ALCH</div>
<div class="select" style="left:253px;top:841px;width:305px">Swiftline</div>
<div class="select" style="left:253px;top:900px;width:305px"></div>
<div class="select" style="left:253px;top:959px;width:305px"></div>
<div class="select" style="left:253px;top:1019px;width:305px">Partials</div>

<div class="slbl" style="left:486px;top:792px">Line Ship Rule</div>
<div class="slbl" style="left:486px;top:851px">Request Date</div>
<div class="slbl" style="left:486px;top:910px">Freight Terms</div>
<div class="slbl" style="left:486px;top:969px">Freight Calc</div>
<div class="slbl" style="left:486px;top:1029px">Custmer Ship To</div>
<div class="select" style="left:701px;top:782px;width:305px;padding-left:17px">Partials</div>
<div class="select" style="left:701px;top:841px;width:305px;padding-left:17px">03/20/2018</div>
<div class="select" style="left:701px;top:900px;width:305px;padding-left:17px">Collect</div>
<div class="select" style="left:701px;top:959px;width:305px"></div>
<div class="select" style="left:701px;top:1019px;width:305px;padding-left:17px">/</div>

<div class="abs hint">Enter Property Values And Click Apply</div>
</body>
</html>
```